Business card for STEADYWAVE

Please design professional business card for IT consulting firm STEADYWAVE INC.
Use logo attached.
Use information from sample qNode business card attached.
replace qnode inc with STEADYWAVE INC.
as well as qnodeinc.com with steadywave.example

```html
<!DOCTYPE html>
<html lang="en">
<head>
<meta charset="utf-8">
<title>STEADYWAVE Business Card</title>
<link href="https://fonts.googleapis.com/css2?family=Montserrat:wght@400;500;600;700&display=swap" rel="stylesheet">
<style>
  :root {
    --backdrop: #3a3532;
    --card-white: #ffffff;
    --card-black: #1b1b1b;
    --ink: #111111;
    --ink-soft: #333333;
    --mark: #7b3fe4;
    --panel-dark: #050505;
    --panel-light: #9a9a9a;
  }
  * { margin: 0; padding: 0; box-sizing: border-box; }
  html, body { width: 1200px; height: 786px; overflow: hidden; }
  body {
    background: var(--backdrop);
    font-family: "Montserrat", sans-serif;
    position: relative;
  }
  .card {
    position: absolute;
    top: 241px;
    width: 530px;
    height: 303px;
    overflow: hidden;
    box-shadow: 0 10px 28px rgba(0,0,0,0.45);
  }
  .card-front { left: 50px; background: var(--card-white); color: var(--ink); }
  .card-back { left: 620px; background: var(--card-black); }

  .wordmark {
    position: absolute;
    display: flex;
    align-items: center;
    gap: 10px;
    font-weight: 700;
    letter-spacing: 4px;
  }
  .wordmark-square { width: 12px; height: 12px; background: var(--mark); }
  .card-front .wordmark { left: 42px; top: 72px; font-size: 30px; color: var(--ink); }

  .person { position: absolute; left: 44px; top: 138px; }
  .person-name { font-size: 17px; font-weight: 700; }
  .person-title { font-size: 11px; color: var(--ink-soft); margin-top: 1px; }

  .contact {
    position: absolute;
    font-size: 11px;
    line-height: 18px;
    color: var(--ink);
    list-style: none;
  }
  .contact .label { font-weight: 700; display: inline-block; width: 16px; }
  .contact-primary { left: 44px; top: 186px; }
  .contact-secondary { left: 240px; top: 140px; }

  .company { position: absolute; left: 44px; top: 238px; }
  .company-name { font-size: 12px; font-weight: 600; letter-spacing: 0.5px; }
  .company-cities { font-size: 11px; color: var(--ink-soft); }

  .back-panel {
    position: absolute;
    background: linear-gradient(90deg, var(--panel-dark), var(--panel-light));
  }
  .panel-top { left: 100px; top: 22px; width: 200px; height: 62px; }
  .panel-middle { left: 40px; top: 84px; width: 180px; height: 100px;
    background: linear-gradient(90deg, #000, #2a2a2a); }
  .panel-bottom { left: 60px; top: 184px; width: 200px; height: 72px;
    background: linear-gradient(90deg, #1a1a1a, #6f6f6f); }
  .panel-tab { left: 22px; top: 40px; width: 28px; height: 44px;
    background: #0d0d0d; }
  .card-back .wordmark { left: 210px; top: 130px; font-size: 30px; color: var(--card-white); }
</style>
</head>
<body>
  <section class="card card-front">
    <div class="wordmark"><span>STEADYWAVE</span><span class="wordmark-square"></span></div>
    <div class="person">
      <div class="person-name">Dorian Halvorsen</div>
      <div class="person-title">General Manager</div>
    </div>
    <ul class="contact contact-secondary">
      <li><span class="label">f.</span>(555) 014-2290</li>
      <li><span class="label">w.</span>www.steadywave.example</li>
    </ul>
    <ul class="contact contact-primary">
      <li><span class="label">o.</span>(555) 014-2290</li>
      <li><span class="label">e.</span>info@steadywave.example</li>
    </ul>
    <div class="company">
      <div class="company-name">STEADYWAVE INC.</div>
      <div class="company-cities">Toronto, Vancouver</div>
    </div>
  </section>

  <section class="card card-back">
    <div class="back-panel panel-tab"></div>
    <div class="back-panel panel-top"></div>
    <div class="back-panel panel-middle"></div>
    <div class="back-panel panel-bottom"></div>
    <div class="wordmark"><span>STEADYWAVE</span><span class="wordmark-square"></span></div>
  </section>
</body>
</html>
```